GLP letterhead

We need a letterhead design for our new company based in Los Angeles called "Gold Lantern Pictures". We develop film and television projects. We work with investors, financiers, film production companies, film distribution and sales companies as well as studios. We would like to incorporate our logo (see attached) but make the letterhead simple and elegant. We need to include: logo, company address, phone number and company website.
Updates

Hello designers, Thanks for your submissions. For our letterhead, we are looking for something more simple and elegant. No heavy bars or lines. Make it feel light and clean. Not a lot of ink on the page. Use the logo and contact info but think "clean", "streamlined" and mostly white paper. Looking forward to seeing more... thanks! Gold Lantern Pictures team

Target Market(s)

Studio executives, talent agents and agencies, financiers, investors.

Industry/Entity Type

It Company

Requirements
Must have
• Gold Lantern Pictures logo (see attached). Logo may be cropped and altered appropriately for elegant letterhead design.
• Please include:
• COMPANY ADDRESS:
• Ridgeway Studio Park
• 2850 Halverson Street
• Tower Annex, 4th Floor
• Manhattan Beach, CA 90412
• COMPANY WEBSITE:
• www.goldlanternpicturesco.example
• COMPANY PHONE NUMBER:
• 310-555-0148

```html
<!DOCTYPE html>
<html lang="en">
<head>
<meta charset="utf-8">
<title>Gold Lantern Pictures — Letterhead</title>
<link rel="stylesheet" href="https://fonts.googleapis.com/css2?family=Open+Sans:wght@400;700&display=swap">
<style>
  :root {
    --strip-tint: #f5f8fa;
    --strip-edge: #cfe9f7;
    --sprocket-blue: #a9dcf5;
    --brand-blue: #1b7fc0;
    --ring-blue: #1ba8ea;
    --tagline-grey: #a7a9ac;
    --paper: #ffffff;
    --contact-text: #6d6e71;
  }
  html, body {
    margin: 0;
    padding: 0;
    overflow: hidden;
    background: var(--paper);
  }
  .letterhead {
    position: relative;
    width: 928px;
    height: 1200px;
    overflow: hidden;
    background: var(--paper);
    font-family: "Open Sans", Arial, sans-serif;
  }
  .film-strip {
    position: absolute;
    left: 0;
    top: 0;
    width: 143px;
    height: 1200px;
  }
  .brand-mark {
    position: absolute;
    left: 40px;
    top: 40px;
    width: 204px;
    height: 204px;
  }
  .brand-name {
    position: absolute;
    left: 252px;
    top: 102px;
    margin: 0;
    font-size: 30px;
    font-weight: 700;
    letter-spacing: 1.5px;
    line-height: 40px;
    color: var(--brand-blue);
    white-space: nowrap;
  }
  .brand-tagline {
    position: absolute;
    left: 254px;
    top: 164px;
    margin: 0;
    font-size: 11.5px;
    font-weight: 400;
    letter-spacing: 3.2px;
    color: var(--tagline-grey);
    white-space: nowrap;
  }
  .contact-block {
    position: absolute;
    left: 58px;
    top: 1146px;
    width: 900px;
    transform: rotate(-90deg);
    transform-origin: top left;
    color: var(--contact-text);
    font-style: normal;
    font-weight: 400;
    font-size: 15px;
    line-height: 24px;
  }
  .contact-line {
    display: flex;
    align-items: center;
    gap: 6px;
    white-space: nowrap;
  }
  .contact-icon {
    width: 11px;
    height: 11px;
    flex: none;
  }
</style>
</head>
<body>
<div class="letterhead">
  <svg class="film-strip" viewBox="0 0 143 1200" aria-hidden="true">
    <rect x="0" y="0" width="143" height="1200" fill="var(--strip-tint)"/>
    <line x1="142.5" y1="0" x2="142.5" y2="1200" stroke="var(--strip-edge)" stroke-width="1"/>
    <g fill="none" stroke="var(--sprocket-blue)" stroke-width="1.5">
      <rect x="18" y="22" width="18" height="18"/><rect x="18" y="66" width="18" height="18"/>
      <rect x="18" y="109" width="18" height="18"/><rect x="18" y="153" width="18" height="18"/>
      <rect x="18" y="196" width="18" height="18"/><rect x="18" y="240" width="18" height="18"/>
      <rect x="18" y="283" width="18" height="18"/><rect x="18" y="327" width="18" height="18"/>
      <rect x="18" y="370" width="18" height="18"/><rect x="18" y="414" width="18" height="18"/>
      <rect x="18" y="457" width="18" height="18"/><rect x="18" y="501" width="18" height="18"/>
      <rect x="18" y="544" width="18" height="18"/><rect x="18" y="588" width="18" height="18"/>
      <rect x="18" y="631" width="18" height="18"/><rect x="18" y="675" width="18" height="18"/>
      <rect x="18" y="718" width="18" height="18"/><rect x="18" y="762" width="18" height="18"/>
      <rect x="18" y="805" width="18" height="18"/><rect x="18" y="849" width="18" height="18"/>
      <rect x="18" y="892" width="18" height="18"/><rect x="18" y="936" width="18" height="18"/>
      <rect x="18" y="979" width="18" height="18"/><rect x="18" y="1023" width="18" height="18"/>
      <rect x="18" y="1066" width="18" height="18"/><rect x="18" y="1110" width="18" height="18"/>
      <rect x="18" y="1153" width="18" height="18"/>
    </g>
  </svg>

  <svg class="brand-mark" viewBox="0 0 204 204" aria-hidden="true">
    <circle cx="102" cy="102" r="100" fill="var(--paper)" stroke="var(--ring-blue)" stroke-width="2"/>
  </svg>

  <h1 class="brand-name">GOLD LANTERN PICTURES</h1>
  <p class="brand-tagline">A MEDIA ENTERTAINMENT COMPANY</p>

  <address class="contact-block">
    <div class="contact-line">
      <svg class="contact-icon" viewBox="0 0 12 12" aria-hidden="true">
        <circle cx="6" cy="6" r="5" fill="none" stroke="currentColor" stroke-width="1.2"/>
        <path d="M1 6h10M6 1c-2.5 3-2.5 7 0 10M6 1c2.5 3 2.5 7 0 10" fill="none" stroke="currentColor" stroke-width="0.9"/>
      </svg>
      <span>www.goldlanternpicturesco.example</span>
    </div>
    <div class="contact-line">
      <svg class="contact-icon" viewBox="0 0 12 12" aria-hidden="true">
        <path d="M3 1.5l2 2.5-1.2 1.2c.7 1.4 1.6 2.3 3 3L8 7l2.5 2-1.2 1.8C5.5 10.5 1.5 6.5 1.2 2.7z" fill="currentColor"/>
      </svg>
      <span>310-555-0148</span>
    </div>
    <div class="contact-line">
      <svg class="contact-icon" viewBox="0 0 12 12" aria-hidden="true">
        <path d="M6 0.8a3.8 3.8 0 0 0-3.8 3.8C2.2 7.5 6 11.2 6 11.2s3.8-3.7 3.8-6.6A3.8 3.8 0 0 0 6 0.8zm0 5.3a1.5 1.5 0 1 1 0-3 1.5 1.5 0 0 1 0 3z" fill="currentColor"/>
      </svg>
      <span>Ridgeway Studio Park, 2850 Halverson Street, Tower Annex, 4th Floor, Manhattan Beach, CA 90412</span>
    </div>
  </address>
</div>
</body>
</html>
```